Professional Training Company Needs a Brochure for a Premium Course

Need a Brochure Design/Registration Form for a Premium Management Course on Decision Making conducted by an ex-CEO of a International Bank.
Needs to have look and feel of the overall Quillbrook Training brand (see website www.quilltrainings.com)

Target Market(s)

C-level Executives of Large Companies, Successful Business Owners/Entrepreneurs

Industry/Entity Type

Professional Service

Font styles to use
Serif

Colors
9bcb3c
add136
cadf82
eaf2ce

Requirements
Must have
• (1) The information contained in the Word Document (Course Information).
• (2) Congruency of look and feel with the Quillbrook Training brand (see website: www.quilltrainings.com. Sister Website is www.quilldirect.co)
• (3) Easy to be adapted for future courses
• (4) Include space for the Trainer's Photo
• (5) Quillbrook Training logos attached
• (6) A registration form at the bottom of the page
Nice to have
• Try to keep this as 2 pager of A4.
Should not have
• (1) Conceptual / illustration stock images e.g., like the neurons and balls in the sample of the old brochure (it feels cheesy)

```html
<!DOCTYPE html>
<html lang="en">
<head>
<meta charset="utf-8">
<title>Quillbrook Training – Course Brochure</title>
<link href="https://fonts.googleapis.com/css2?family=Arimo:wght@400;700&display=swap" rel="stylesheet">
<style>
:root{
  --green:#9bcb3c;
  --green-deep:#84b52a;
  --green-bright:#add136;
  --green-soft:#cadf82;
  --green-pale:#eaf2ce;
  --ink:#2b2b2b;
  --muted:#666;
  --line:#9bcb3c;
  --white:#fff;
}
*{box-sizing:border-box;margin:0;padding:0}
html,body{width:882px;height:1200px;overflow:hidden;background:var(--white)}
body{font-family:"Arimo",Arial,sans-serif;color:var(--ink);position:relative}
.city-banner{position:absolute;left:435px;top:0;width:447px;height:380px;
  background:linear-gradient(180deg,#b7bdc4 0%,#d3d7dc 45%,#eef0f2 80%,#ffffff 100%)}
.profile-column{position:absolute;left:0;top:0;width:435px;height:1020px;background:var(--green);
  padding:282px 40px 0 44px;color:var(--white)}
.trainer-photo{position:absolute;left:112px;top:100px;width:118px;height:166px;
  background:linear-gradient(160deg,#8a5a48,#3e3430 60%,#2a2a2e);border:3px solid var(--white)}
.profile-title{font-size:22px;font-weight:700;margin-bottom:10px}
.profile-text{font-size:15.5px;line-height:1.45;margin-bottom:16px;text-align:justify}
.brand{position:absolute;left:680px;top:200px;display:flex;align-items:center;gap:8px}
.brand-dot{width:26px;height:26px;border-radius:50%;background:var(--green)}
.brand-name{font-size:17px;font-weight:700;color:var(--green-deep);line-height:1.05;width:120px}
.registration{position:absolute;left:470px;top:390px;width:380px}
.registration h2{font-size:21px;font-weight:700;color:var(--ink);margin-bottom:22px}
.field{border-bottom:1.5px solid var(--line);height:58px;padding-top:26px;font-size:13.5px;color:var(--muted)}
.field:first-of-type{padding-top:6px;height:44px}
.field b{color:var(--ink)}
.terms{position:absolute;left:44px;top:1032px;width:800px;font-size:8.6px;line-height:1.33;color:var(--ink)}
.terms b{font-weight:700}
.footer-bar{position:absolute;left:0;top:1150px;width:882px;height:50px;background:var(--green);
  display:flex;align-items:center;padding-left:115px;gap:60px;color:var(--white);font-size:19px}
.contact{display:flex;align-items:center;gap:10px}
</style>
</head>
<body>
<div class="city-banner" role="img" aria-label="City skyline photograph fading to white"></div>

<section class="profile-column">
  <div class="trainer-photo" role="img" aria-label="Trainer portrait photograph"></div>
  <h1 class="profile-title">Faculty Profile</h1>
  <p class="profile-text">Rajan Mehtani is based in the US (New York) and Asia (Kuala Lumpur). An exceptionally talented and versatile business leader who has successfully led businesses and diverse teams internationally for over 30 years, he has acquired a unique perspective and ability to blend Asian and Western management practices and culture from his extensive and deep global experience.</p>
  <p class="profile-text">Prior to his 19 years across most countries in Asia (including being based in Hong Kong, India and Malaysia), he has spent over 15 years in New York and Boston and conducted business in Europe and Latin America. His experience is drawn from working with multiple blue-chip institutions including some of the largest global and regional companies (Orbis Bank, Harbor Union Bank and Meridian Chartered Bank) and with companies and management teams across a wide variety of industries and markets.</p>
  <p class="profile-text">His leadership insights are based on direct senior line management experience in developed and emerging markets, small and mature businesses and from navigating within complex organizational structures. He has managed small and large (over 3000) groups of employees.</p>
</section>

<div class="brand"><span class="brand-dot"></span><span class="brand-name">QUILLBROOK TRAINING</span></div>

<section class="registration">
  <h2>Registration form</h2>
  <div class="field"><b>Upcoming dates</b> (City) (Date)</div>
  <div class="field">No of participants:</div>
  <div class="field">Name:</div>
  <div class="field">Company:</div>
  <div class="field">Role in Company:</div>
  <div class="field">Years of Work Experience:</div>
  <div class="field">Email:</div>
  <div class="field">Phone:</div>
</section>

<section class="terms">
  <p><b>Booking terms and conditions (the course fee is [xxx])</b></p>
  <p><b>Registration and Confirmation Policy</b></p>
  <p>50% of the course fee to be deposited to secure your registration.</p>
  <p>The seat is confirmed only once full payment reaches us before the course date.</p>
  <p>The balance of 50% is payable no later than 2 weeks before the course starts.</p>
  <p><b>Cancellation and Transfer Policy</b></p>
  <p>Cancellations received 2 weeks before the start date are refunded less a handling fee.</p>
  <p>Cancellations within 2 weeks of the course date are not refundable but may be transferred.</p>
  <p><b>Early Bird and Group Rates</b></p>
  <p>Group registrations of three or more receive a reduced rate; please contact us for details.</p>
</section>

<footer class="footer-bar">
  <span class="contact">
    <svg width="18" height="18" viewBox="0 0 24 24" aria-hidden="true"><path fill="#fff" d="M6.6 10.8a15 15 0 0 0 6.6 6.6l2.2-2.2c.3-.3.7-.4 1-.2 1.1.4 2.3.6 3.6.6.6 0 1 .4 1 1V20c0 .6-.4 1-1 1A17 17 0 0 1 3 4c0-.6.4-1 1-1h3.5c.6 0 1 .4 1 1 0 1.3.2 2.5.6 3.6.1.3 0 .7-.2 1z"/></svg>
    KL: +603 5550 1942
  </span>
  <span class="contact">
    <svg width="20" height="16" viewBox="0 0 24 18" aria-hidden="true"><rect x="1" y="1" width="22" height="16" fill="none" stroke="#fff" stroke-width="2"/><path d="M1 1l11 9 11-9" fill="none" stroke="#fff" stroke-width="2"/></svg>
    enquiry@quilltrainings.com
  </span>
</footer>
</body>
</html>
```